2022 Lindenfield Cardiology Annual Christmas Post Card for Patients

This is our annual christmas card that will be mailed out to our patients. We are a cardiology physician clinic. Size of the card is 8 inches in width and 5 inches in height. I need a blank white space in the bottom right corner of the back of the card measuring at least 3 1/2 inch in width and 3 inches in height for address and postage to be placed. It should include our clinic group photo of everyone, provider group photo on back, logo, address, phone, fax, email, and web address. Our address is 218 Harrow Ln. Ste. B, Alder Cove, TX 77000. Phone is 832-614-2287, Fax is 832-614-2288. Web address is www.lindenfieldcardio.example. Email address is info@lindenfieldcardio.example . We would like it to say "Happy Holidays from the Physicians and Staff at Lindenfield Cardiology".
Should be able to post the same on website and social media with holiday message. Our office colors are red and black but all colors could be considered.

Target Market(s)

Our Patients

Industry/Entity Type

Healthcare

Font styles to use
Script

Colors
EB3D1F
EC4F4E
F09395
F8D3D4
FCEDEE

Requirements
Must have
• All info listed in brief
Nice to have
• Open to suggestions
Should not have
• The words "Merry Christmas"

```html
<!DOCTYPE html>
<html lang="en">
<head>
<meta charset="utf-8">
<title>Lindenfield Cardiology – Holiday Postcard</title>
<link href="https://fonts.googleapis.com/css2?family=Allura&family=Montserrat:wght@600;700&family=Roboto+Condensed:wght@400;500&display=swap" rel="stylesheet">
<style>
  :root {
    --bg: #e3e3e4;
    --red: #c21e2c;
    --red-bright: #ec2a2e;
    --red-deep: #a5141f;
    --ink: #1d1d1f;
    --charcoal: #3c3c40;
    --white: #ffffff;
    --rule: #b9b9bd;
  }
  * { margin: 0; padding: 0; box-sizing: border-box; }
  html, body { width: 980px; height: 1200px; overflow: hidden; }
  body { background: var(--bg); position: relative; font-family: "Roboto Condensed", sans-serif; }

  /* ---------- Front ---------- */
  .card-front {
    position: absolute; left: 114px; top: 100px; width: 766px; height: 479px;
    background: radial-gradient(ellipse 55% 60% at 50% 42%, var(--red-bright) 0%, var(--red) 55%, var(--red-deep) 100%);
    overflow: hidden;
  }
  .brand-tab {
    position: absolute; left: 271px; top: 0; width: 222px; height: 88px;
    background: var(--white); border-radius: 0 0 14px 14px;
    display: flex; align-items: center; justify-content: center; gap: 8px;
  }
  .brand-dot { width: 12px; height: 12px; border-radius: 50%; background: var(--red); flex: none; }
  .brand-name {
    font-family: "Montserrat", sans-serif; font-weight: 700; color: var(--red);
    font-size: 15px; line-height: 1.15; text-transform: uppercase; letter-spacing: 0.5px;
  }
  .front-greeting {
    position: absolute; left: 0; right: 0; top: 96px; text-align: center;
    font-family: "Allura", cursive; font-weight: 400; color: var(--white); font-size: 108px; line-height: 1;
  }
  .front-photo {
    position: absolute; left: 56px; top: 197px; width: 660px; height: 230px;
    background: linear-gradient(180deg, rgba(60,30,35,0.35) 0%, rgba(245,240,240,0.85) 55%, rgba(240,236,236,0.9) 100%);
    border-radius: 90px 90px 0 0;
  }
  .front-rule {
    position: absolute; left: 62px; right: 62px; top: 428px; height: 1px; background: var(--white);
  }
  .front-rule::before, .front-rule::after {
    content: ""; position: absolute; top: -2px; width: 5px; height: 5px; border-radius: 50%; background: var(--white);
  }
  .front-rule::before { left: 0; } .front-rule::after { right: 0; }
  .front-caption {
    position: absolute; left: 0; right: 0; top: 438px; text-align: center;
    font-family: "Montserrat", sans-serif; font-weight: 600; font-size: 14px; letter-spacing: 1.5px;
    color: var(--white); text-transform: uppercase;
  }

  /* ---------- Back ---------- */
  .card-back {
    position: absolute; left: 117px; top: 640px; width: 766px; height: 478px;
    background: var(--white); overflow: hidden;
  }
  .back-swoosh { position: absolute; left: 0; top: 0; }
  .back-greeting {
    position: absolute; left: 32px; top: 18px;
    font-family: "Allura", cursive; font-weight: 400; color: var(--white); font-size: 72px; line-height: 1;
  }
  .snapshot {
    position: absolute; left: 35px; top: 96px; width: 355px; height: 258px;
    background: var(--white); transform: rotate(-3deg);
    box-shadow: 0 10px 18px rgba(0,0,0,0.28);
    padding: 10px 10px 0;
  }
  .snapshot-photo {
    width: 335px; height: 206px;
    background: linear-gradient(180deg, #8c2a2a 0%, #a0393a 45%, #c9b9b0 80%, #d7cfc7 100%);
  }
  .snapshot-caption {
    margin-top: 10px; text-align: right; font-size: 12px; color: var(--ink); text-transform: uppercase; white-space: nowrap;
  }
  .stamp-box {
    position: absolute; left: 638px; top: 37px; width: 91px; height: 90px; border: 1px solid #8d8d92;
  }
  .address-line { position: absolute; left: 460px; width: 269px; height: 1px; background: var(--rule); }
  .contact {
    position: absolute; right: 345px; top: 372px; text-align: right; font-style: normal;
    font-size: 14px; color: var(--ink); line-height: 21px;
  }
  .contact-row { display: flex; justify-content: flex-end; align-items: center; gap: 12px; }
  .contact-item { display: inline-flex; align-items: center; gap: 4px; white-space: nowrap; }
  .contact-item svg { width: 14px; height: 14px; flex: none; }
  .back-brand {
    position: absolute; left: 460px; top: 378px; display: flex; align-items: center; gap: 10px;
  }
  .back-brand .brand-dot { width: 16px; height: 16px; }
  .back-brand .brand-name { font-size: 22px; line-height: 1.1; }
  .bar-dark { position: absolute; left: 0; top: 467px; width: 441px; height: 11px; background: var(--charcoal); }
  .bar-red { position: absolute; left: 446px; top: 467px; width: 320px; height: 11px; background: var(--red); }
</style>
</head>
<body>

<section class="card-front">
  <div class="brand-tab">
    <span class="brand-dot"></span>
    <span class="brand-name">Lindenfield<br>Cardiology</span>
  </div>
  <h1 class="front-greeting">Happy Holidays</h1>
  <div class="front-photo" role="img" aria-label="Group photo of the Lindenfield Cardiology physicians and staff in white coats and scrubs"></div>
  <div class="front-rule"></div>
  <p class="front-caption">From the Physicians and Staff at Lindenfield Cardiology</p>
</section>

<section class="card-back">
  <svg class="back-swoosh" width="766" height="300" viewBox="0 0 766 300" aria-hidden="true">
    <defs>
      <radialGradient id="swooshFill" cx="35%" cy="30%" r="70%">
        <stop offset="0" stop-color="#ec2a2e"/>
        <stop offset="1" stop-color="#a5141f"/>
      </radialGradient>
    </defs>
    <path d="M0 0 H508 C478 66 430 96 340 110 C200 132 55 180 0 282 Z" fill="url(#swooshFill)"/>
  </svg>
  <h2 class="back-greeting">Happy Holidays</h2>

  <figure class="snapshot">
    <div class="snapshot-photo" role="img" aria-label="Group photo of the Lindenfield Cardiology physicians seated in front of a red wall"></div>
    <figcaption class="snapshot-caption">From the Physicians and Staff at Lindenfield Cardiology</figcaption>
  </figure>

  <div class="stamp-box"></div>
  <div class="address-line" style="top:182px"></div>
  <div class="address-line" style="top:223px"></div>
  <div class="address-line" style="top:264px"></div>
  <div class="address-line" style="top:305px"></div>

  <address class="contact">
    <div class="contact-row">
      <span class="contact-item">
        <svg viewBox="0 0 14 14"><circle cx="7" cy="7" r="7" fill="#c21e2c"/><path d="M7 3.2a2.3 2.3 0 0 0-2.3 2.3C4.7 7.3 7 10.6 7 10.6s2.3-3.3 2.3-5.1A2.3 2.3 0 0 0 7 3.2z" fill="#fff"/><circle cx="7" cy="5.5" r="0.9" fill="#c21e2c"/></svg>
        218 Harrow Ln. Ste. B, Alder Cove, TX 77000
      </span>
    </div>
    <div class="contact-row">
      <span class="contact-item">
        <svg viewBox="0 0 14 14"><circle cx="7" cy="7" r="7" fill="#c21e2c"/><path d="M4.6 3.6l1.2-.3.8 1.8-.8.6c.4.9 1 1.5 1.9 1.9l.6-.8 1.8.8-.3 1.2c-3 .2-5.4-2.2-5.2-5.2z" fill="#fff"/></svg>
        832-614-2287
      </span>
      <span class="contact-item">
        <svg viewBox="0 0 14 14"><circle cx="7" cy="7" r="7" fill="#c21e2c"/><rect x="4.5" y="3.3" width="5" height="2.4" fill="#fff"/><rect x="3.4" y="6" width="7.2" height="3.4" rx=".6" fill="#fff"/><rect x="4.5" y="8.6" width="5" height="2.2" fill="#fff"/></svg>
        832-614-2288
      </span>
    </div>
    <div class="contact-row">
      <span class="contact-item">
        <svg viewBox="0 0 14 14"><circle cx="7" cy="7" r="7" fill="#c21e2c"/><circle cx="7" cy="7" r="3.6" fill="none" stroke="#fff" stroke-width=".9"/><ellipse cx="7" cy="7" rx="1.5" ry="3.6" fill="none" stroke="#fff" stroke-width=".8"/><path d="M3.4 7h7.2" stroke="#fff" stroke-width=".8"/></svg>
        www.lindenfieldcardio.example
      </span>
      <span class="contact-item">
        <svg viewBox="0 0 14 14"><circle cx="7" cy="7" r="7" fill="#c21e2c"/><rect x="3.6" y="4.6" width="6.8" height="4.8" fill="#fff"/><path d="M3.6 4.6L7 7.4l3.4-2.8" fill="none" stroke="#c21e2c" stroke-width=".8"/></svg>
        info@lindenfieldcardio.example
      </span>
    </div>
  </address>

  <div class="back-brand">
    <span class="brand-dot"></span>
    <span class="brand-name">Lindenfield<br>Cardiology</span>
  </div>

  <div class="bar-dark"></div>
  <div class="bar-red"></div>
</section>

</body>
</html>
```